Velmora Roasters

Full Shopify site .
About page

Merch page
Tshirts, hats, mugs

Coffee page
-sections
Single origin
Tamblin series
Quillet series
Decaf

VelmoraQ page
Cold brew
Coffee liquor
Absinthe Coffee

```html
<!DOCTYPE html>
<html lang="en">
<head>
<meta charset="utf-8">
<title>Velmora Roasters</title>
<link href="https://fonts.googleapis.com/css2?family=Montserrat:wght@400;500;600;700&family=Playfair+Display:wght@500;600;700&display=swap" rel="stylesheet">
<style>
:root{
  --red:#e0393e;
  --red-dark:#c92d33;
  --ink:#141414;
  --blush:#fcecf0;
  --blush-deep:#f6d3dc;
  --card:#ffffff;
  --muted:#3a3a3a;
  --stage:#b3b3b3;
  --serif:'Playfair Display', Georgia, serif;
  --sans:'Montserrat', Arial, sans-serif;
}
*{box-sizing:border-box;margin:0;padding:0}
html,body{width:1200px;height:3812px;overflow:hidden}
body{background:var(--stage);font-family:var(--sans);color:var(--ink)}
.page{position:absolute;left:98px;top:104px;width:1005px;height:3610px;background:#fff;box-shadow:0 4px 18px rgba(0,0,0,.25);overflow:hidden}
.section{position:absolute;left:0;width:1005px}
.abs{position:absolute}
.center-x{left:0;width:100%;text-align:center}

/* nav */
.nav{top:0;height:63px;background:#fff}
.brand{left:62px;top:10px;display:flex;align-items:center;gap:10px}
.brand-dot{width:44px;height:44px;border-radius:50%;background:var(--red)}
.brand-name{font-family:var(--sans);font-weight:700;font-size:17px;color:var(--ink)}
.menu{left:383px;top:23px;display:flex;gap:0;font-family:var(--serif);font-size:12px;font-weight:600;letter-spacing:.3px}
.menu a{color:var(--ink);text-decoration:none;margin-right:24px}
.pill{left:853px;top:19px;width:82px;height:26px;border-radius:13px;background:var(--red);color:#fff;font-family:var(--serif);font-size:12px;font-weight:600;display:flex;align-items:center;justify-content:center}

/* hero */
.hero{top:63px;height:549px}
.hero-art{inset:0;background:linear-gradient(100deg,#2d3a5c 0%,#c76a8e 30%,#ee9fb4 55%,#f2b3c3 75%,#2a1a22 100%)}
.hero-sun{left:142px;top:66px;width:310px;height:310px;border-radius:50%;background:var(--red)}
.hero-title{left:142px;top:100px;width:310px;text-align:center;font-family:var(--serif);font-weight:600;font-size:48px;line-height:43px;color:#1a0a0c}
.hero-kicker{left:142px;top:281px;width:310px;text-align:center;font-weight:700;font-size:25px;line-height:28px;color:#1a0a0c}
.hero-lead{left:258px;top:351px;width:520px;text-align:center;font-size:22px;line-height:30px;color:#fff}
.hero-lead b{font-weight:700}
.btn-dark{left:394px;top:446px;width:247px;height:41px;border-radius:21px;background:#0d0d0d;color:#fff;font-weight:700;font-size:15px;display:flex;align-items:center;justify-content:center}

/* shared headings */
.mark{width:48px;height:48px;border-radius:50%;background:var(--red);left:478px}
.eyebrow{font-weight:700;font-size:22px;color:var(--red);display:flex;justify-content:center;align-items:center;gap:8px;height:26px}
.eyebrow::before,.eyebrow::after{content:"";width:30px;height:2px;background:var(--red)}
.title{font-family:var(--serif);font-weight:500;font-size:50px;line-height:54px;color:var(--ink)}

/* collections */
.collections{top:612px;height:569px;background:linear-gradient(90deg,#f9d9e1 0%,var(--blush) 25%,#fdf2f5 60%,var(--blush) 100%)}
.col-card{top:239px;width:172px;height:253px;background:var(--card);border-radius:4px;box-shadow:0 2px 8px rgba(0,0,0,.12);overflow:hidden}
.col-img{height:123px}
.col-body{padding:12px 15px 0}
.col-body h3{font-size:16px;font-weight:700;margin-bottom:5px}
.col-body p{font-size:11px;line-height:15px;color:var(--muted);height:62px}
.link{font-size:11px;font-weight:700;color:var(--red);display:flex;align-items:center;gap:5px;margin-top:4px}

/* bundles */
.bundles{top:1181px;height:783px;background:#fff}
.lead{font-size:19px;color:var(--ink)}
.bundle{top:273px;width:231px;height:434px;background:#fbf0f3;border-radius:4px;box-shadow:0 2px 8px rgba(0,0,0,.12);overflow:hidden;text-align:center}
.bundle-img{height:237px;position:relative}
.badge{position:absolute;right:10px;top:14px;background:var(--red);color:#fff;font-size:11px;font-weight:600;padding:4px 8px;border-radius:3px}
.bundle .kind{margin-top:26px;font-size:15px;font-weight:600;color:var(--red)}
.bundle h3{font-size:20px;font-weight:700;margin-top:4px}
.bundle p{font-size:11px;line-height:15px;color:var(--muted);padding:0 24px;margin-top:4px;height:46px}
.price{font-size:23px;font-weight:700;margin-top:6px}
.price s{font-size:15px;font-weight:400;color:var(--muted);margin-left:4px}
.btn-red{display:inline-flex;align-items:center;justify-content:center;background:var(--red);color:#fff;font-weight:700;font-size:11px;border-radius:3px}
.bundle .btn-red{width:107px;height:24px;margin-top:8px}

/* subscribe */
.subscribe{top:1964px;height:418px;background:var(--blush)}
.sub-col{left:124px;width:320px;text-align:center}
.sub-text{font-size:22px;line-height:29px}
.sub-text b{font-weight:700}
.sub-btn{left:185px;top:301px;width:198px;height:36px;border-radius:18px;font-size:17px}
.sub-art{left:472px;top:93px;width:407px;height:229px;border-radius:6px;background:radial-gradient(ellipse at 50% 55%,#c8955d 0%,#e6c8a3 40%,var(--blush) 75%)}

/* merch */
.merch{top:2382px;height:696px;background:#fff}
.merch-card{top:246px;width:231px;height:373px;background:#f6f6f6;border-radius:4px;box-shadow:0 2px 8px rgba(0,0,0,.12);overflow:hidden;text-align:center}
.merch-img{height:235px}
.merch-card h3{font-size:16px;font-weight:700;margin-top:22px}
.merch-card p{font-size:11px;line-height:15px;color:var(--muted);padding:0 22px;margin-top:4px;height:48px}
.merch-card .link{justify-content:center;margin-top:6px}

/* story */
.story{top:3078px;height:478px;background:var(--blush)}
.story-art{left:0;top:0;width:520px;height:478px;background:linear-gradient(100deg,var(--red) 0%,var(--red) 45%,#f3b6c7 75%,var(--blush) 100%)}
.story-col{left:550px;width:318px}
.story h4{font-size:15px;font-weight:700}
.story p{font-size:11px;line-height:15px;color:var(--muted)}
.story-btn{left:550px;top:381px;width:107px;height:24px;border-radius:12px}

/* footer */
.footer{top:3556px;height:54px;display:flex;align-items:center;justify-content:center;font-size:11px;color:var(--ink);background:#fff}
</style>
</head>
<body>
<div class="page">

  <header class="section nav">
    <div class="abs brand"><span class="brand-dot"></span><span class="brand-name">Velmora Roasters</span></div>
    <nav class="abs menu"><a>HOME</a><a>ABOUT</a><a>COFFEE</a><a>VELMORAQ</a><a>MERCH</a><a>SUBSCRIPTION</a></nav>
    <div class="abs pill">CONTACT</div>
  </header>

  <section class="section hero">
    <div class="abs hero-art" role="img" aria-label="Illustration of a silhouetted warrior holding a coffee cup beside a lake, mountains and a blossoming cherry tree in pink tones"></div>
    <div class="abs hero-sun"></div>
    <h1 class="abs hero-title">WHERE<br>COFFEE<br>MEETS<br>ART</h1>
    <div class="abs hero-kicker">FROM BLOSSOM<br>TO BREW</div>
    <p class="abs hero-lead"><b>Experience</b> the harmony of<br>Japanese <b>tradition</b> and specialty<br><b>coffee culture</b>.</p>
    <div class="abs btn-dark">DISCOVER OUR COFFEES</div>
  </section>

  <section class="section collections">
    <div class="abs mark" style="top:78px"></div>
    <div class="abs center-x eyebrow" style="top:141px">OUR</div>
    <h2 class="abs center-x title" style="top:164px">COLLECTIONS</h2>

    <article class="abs col-card" style="left:124px">
      <div class="col-img" role="img" aria-label="Botanical illustration of coffee cherries on a branch" style="background:linear-gradient(135deg,#efe3c4,#7c9a4a 60%,#c2372e)"></div>
      <div class="col-body"><h3>Single Origin</h3><p>Explore traceable beans from distinct regions, roasted to reveal their unique terroir.</p><div class="link">Learn More →</div></div>
    </article>
    <article class="abs col-card" style="left:319px">
      <div class="col-img" role="img" aria-label="Botanical illustration of coffee blossoms and ripe cherries" style="background:linear-gradient(135deg,#e9e2cf,#9aa877 55%,#d4573a)"></div>
      <div class="col-body"><h3>Tamblin Series</h3><p>Delicate florals and refined sweetness – the legendary Tamblin varietal at its peak.</p><div class="link">Learn More →</div></div>
    </article>
    <article class="abs col-card" style="left:513px">
      <div class="col-img" role="img" aria-label="Ink painting of a lone warrior before a misty pagoda" style="background:linear-gradient(180deg,#8a8a8a,#3a3a3a 70%,#1a1a1a)"></div>
      <div class="col-body"><h3>Quillet Series</h3><p>Our signature blends – bold and adventurous, inspired by the spirit of the wandering ronin.</p><div class="link">Learn More →</div></div>
    </article>
    <article class="abs col-card" style="left:707px">
      <div class="col-img" role="img" aria-label="Preview of the VelmoraQ web pages" style="background:linear-gradient(180deg,#f4d9df,#e9e9e9 50%,#2a2a2a)"></div>
      <div class="col-body"><h3>VelmoraQ</h3><p>A limited series of cold brews and coffee spirits – fearless fusions for the adventurous palate.</p><div class="link">Explore VelmoraQ →</div></div>
    </article>
  </section>

  <section class="section bundles">
    <div class="abs mark" style="top:78px"></div>
    <div class="abs center-x eyebrow" style="top:141px">BUNDLES</div>
    <h2 class="abs center-x title" style="top:165px">BUNDLES &amp; COMBOS</h2>
    <p class="abs center-x lead" style="top:220px">Enjoy curated combinations of our finest coffee and lifestyle products.</p>

    <article class="abs bundle" style="left:124px">
      <div class="bundle-img" role="img" aria-label="Coffee bag and mug with cherry blossoms and roasted beans" style="background:linear-gradient(160deg,#f4b6c4,#f9e7ea 50%,#6b3a22)"><span class="badge">Save 15%</span></div>
      <div class="kind">Starter Bundle</div><h3>Coffee + Mug</h3>
      <p>Perfect introduction to Velmora Roasters. Enjoy a balanced brew with our signature mug.</p>
      <div class="price">$35<s>$40</s></div>
      <span class="btn-red">ADD TO CART</span>
    </article>
    <article class="abs bundle" style="left:386px">
      <div class="bundle-img" role="img" aria-label="White t-shirt with cherry blossom print beside a coffee bag" style="background:linear-gradient(160deg,#f4b6c4,#f7f3f3 50%,#c9414a)"><span class="badge">Save 15%</span></div>
      <div class="kind">Lifestyle Bundle</div><h3>Coffee + T-Shirt</h3>
      <p>Wear your passion and enjoy premium coffee. A perfect blend of style and taste.</p>
      <div class="price">$50<s>$60</s></div>
      <span class="btn-red">ADD TO CART</span>
    </article>
    <article class="abs bundle" style="left:648px">
      <div class="bundle-img" role="img" aria-label="Black coffee bag and black cap before a misty pagoda" style="background:linear-gradient(160deg,#c24045,#6e6e6e 40%,#1c1c1c)"><span class="badge">Save 15%</span></div>
      <div class="kind">Quillet Bundle</div><h3>Quillet Coffee + Cap</h3>
      <p>Bold and fearless. Inspired by the wandering samurai. A strong blend with a signature cap.</p>
      <div class="price">$60<s>$75</s></div>
      <span class="btn-red">ADD TO CART</span>
    </article>
  </section>

  <section class="section subscribe">
    <div class="abs mark" style="top:79px;left:260px"></div>
    <div class="abs sub-col eyebrow" style="top:142px">SUBSCRIBE</div>
    <h2 class="abs sub-col title" style="top:166px">&amp; SAVE</h2>
    <p class="abs sub-col sub-text" style="top:222px">Get <b>fresh coffee</b> delivered monthly and <b>save up to 15%</b></p>
    <div class="abs btn-red sub-btn">SUBSCRIBE NOW</div>
    <div class="abs sub-art" role="img" aria-label="Coffee delivery box with a save 15% tag, a cup of coffee, beans and arrows"></div>
  </section>

  <section class="section merch">
    <div class="abs mark" style="top:77px"></div>
    <div class="abs center-x eyebrow" style="top:140px">MERCH</div>
    <h2 class="abs center-x title" style="top:163px">&amp; LIFESTYLE</h2>

    <article class="abs merch-card" style="left:124px">
      <div class="merch-img" role="img" aria-label="White t-shirt with cherry blossom artwork" style="background:linear-gradient(160deg,#f4f4f4,#fde6ec 60%,#f1f1f1)"></div>
      <h3>T-Shirts</h3><p>Soft, stylish tees featuring our iconic sakura artwork. Wear your love for coffee.</p><div class="link">Shop T-Shirts →</div>
    </article>
    <article class="abs merch-card" style="left:386px">
      <div class="merch-img" role="img" aria-label="Black cap with embroidered blossom emblem" style="background:linear-gradient(160deg,#6d6d6d,#1e1e1e 70%)"></div>
      <h3>Hats</h3><p>Complete your look with our embroidered caps – subtle yet statement making.</p><div class="link">Shop Hats →</div>
    </article>
    <article class="abs merch-card" style="left:648px">
      <div class="merch-img" role="img" aria-label="White mug with printed blossom emblem" style="background:linear-gradient(160deg,#f7f7f7,#ececec 60%,#f3f3f3)"></div>
      <h3>Mugs</h3><p>Enjoy your brew in beautiful mugs adorned with our signature logo.</p><div class="link">Shop Mugs →</div>
    </article>
  </section>

  <section class="section story">
    <div class="abs story-art" role="img" aria-label="Ink painting of a cherry blossom tree on a red background"></div>
    <div class="abs mark" style="top:77px;left:605px"></div>
    <div class="abs eyebrow" style="top:136px;left:530px;width:198px">OUR</div>
    <h2 class="abs title" style="top:161px;left:530px;width:198px;text-align:center">STORY</h2>
    <h4 class="abs story-col" style="top:219px">The Art of Roasting</h4>
    <p class="abs story-col" style="top:242px">Velmora Roasters was born from a passion for craftsmanship and culture. Inspired by the fleeting beauty of cherry blossoms, we honour the delicate balance between precision and artistry in every roast.</p>
    <p class="abs story-col" style="top:318px">From our humble beginnings to our ongoing journey, we invite you to share in our story and savour the flavours crafted with care.</p>
    <div class="abs btn-red story-btn">READ MORE</div>
  </section>

  <footer class="section footer">© 2026 Velmora Roasters. Crafted with passion in Lahore.</footer>
</div>
</body>
</html>
```